Assessment Report cover design and formatting

This report is for senior executives and provides leaders with detailed insight into their capabilities and skills. The cover should have space for the date and name of the person doing the assessment. We are looking to modernise the report cover design. We would like the report to be our company colours if possible. The work will likely expand once the cover is done to other parts of the report, ie. the format and layout of the report etc.

Company colours:
Primary colours:
• Blue #0D47A1, #115CD0, #90B6ED, #EEf3FB
• Green #0D91A1, #47A10D, #324C196, #0DA11D
Additional colours:
• Purple #A10D91
• Brown #A1670D
• Red #A10D47

Target Market(s)

Executives

Industry/Entity Type

Consulting, leadership development

Colors
0094D4
00A9DD
6FCCEA
C7EBF8
E9F6FB
00AB8E
00BBA5
67D7C9
C6EFE9
E9F9F6
E54698
E96AAD
F1A4CE
F9D9EA
FCEFF6
6B429C
8869AF
B7A5CE
E3DAEB
F3F0F8

Requirements
Must have
• The report cover should have space for name of user, the date and company logo. Cover should be in A4 size.

```html
<!DOCTYPE html>
<html lang="en">
<head>
<meta charset="utf-8">
<title>Growth Leader Assessment — Insight Report</title>
<link href="https://fonts.googleapis.com/css2?family=Fira+Sans:wght@400;600&display=swap" rel="stylesheet">
<style>
  :root {
    --paper: #ffffff;
    --soft-grey: #efefef;
    --ink-grey: #4a4a4a;
    --rule-grey: #555555;
    --brand-blue: #0d47a1;
    --brand-navy: #0f3d96;
    --grad-green: #2ea674;
    --grad-teal: #2a9196;
    --grad-blue: #3d63b4;
    --sky-light: #eef1f5;
    --sky-mid: #b9c7da;
    --tower-blue: #3d5a80;
  }
  * { margin: 0; padding: 0; box-sizing: border-box; }
  html, body { width: 848px; height: 1200px; overflow: hidden; background: var(--paper); }
  .cover {
    position: relative;
    width: 848px;
    height: 1200px;
    overflow: hidden;
    background: var(--paper);
    font-family: "Fira Sans", sans-serif;
  }
  .cover__texture { position: absolute; left: 0; top: 0; width: 540px; height: 500px; }
  .cover__shapes { position: absolute; inset: 0; }
  .cover__photo { position: absolute; left: 460px; top: 333px; width: 582px; height: 582px; }
  .title { position: absolute; left: 52px; top: 154px; }
  .title__main {
    display: block;
    font-weight: 600;
    font-size: 84px;
    line-height: 1;
    letter-spacing: 0.5px;
    background: linear-gradient(90deg, var(--grad-green) 0%, var(--grad-teal) 45%, var(--grad-blue) 100%);
    -webkit-background-clip: text;
    background-clip: text;
    color: transparent;
  }
  .title__sub {
    display: block;
    margin-top: 18px;
    font-weight: 400;
    font-size: 55px;
    line-height: 1;
    letter-spacing: 0.5px;
    color: var(--ink-grey);
  }
  .recipient { position: absolute; left: 51px; top: 999px; }
  .recipient__heading {
    font-weight: 600;
    font-size: 32px;
    line-height: 1;
    color: var(--brand-blue);
    margin-bottom: 26px;
  }
  .recipient__field {
    display: flex;
    align-items: flex-end;
    font-size: 21px;
    color: var(--ink-grey);
    height: 26px;
    margin-bottom: 16px;
  }
  .recipient__label { width: 69px; }
  .recipient__line { width: 192px; border-bottom: 1.5px solid var(--ink-grey); margin-bottom: 4px; }
  .brand {
    position: absolute;
    left: 536px;
    top: 1016px;
    width: 256px;
    color: var(--brand-navy);
    font-weight: 400;
    text-align: center;
  }
  .brand__name { font-size: 31px; line-height: 1.15; letter-spacing: 3px; }
  .brand__tagline { font-size: 14px; letter-spacing: 3px; margin-top: 6px; }
</style>
</head>
<body>
<main class="cover">
  <svg class="cover__texture" viewBox="0 0 540 500" role="img" aria-label="Decorative pattern of soft grey circles">
    <defs>
      <radialGradient id="textureGradient" cx="0.5" cy="0.45" r="0.6">
        <stop offset="0" stop-color="var(--soft-grey)"/>
        <stop offset="1" stop-color="var(--paper)"/>
      </radialGradient>
    </defs>
    <rect width="540" height="500" fill="url(#textureGradient)"/>
  </svg>

  <svg class="cover__shapes" width="848" height="1200" viewBox="0 0 848 1200" aria-hidden="true">
    <circle class="base-disc" cx="30" cy="1190" r="450" fill="var(--soft-grey)"/>
    <circle class="photo-frame" cx="751" cy="624" r="312" fill="none" stroke="var(--rule-grey)" stroke-width="2"/>
  </svg>

  <svg class="cover__photo" viewBox="0 0 582 582" role="img" aria-label="Photograph looking up at glass office towers against a pale sky">
    <defs>
      <radialGradient id="skyGradient" cx="0.45" cy="0.35" r="0.75">
        <stop offset="0" stop-color="var(--sky-light)"/>
        <stop offset="0.55" stop-color="var(--sky-mid)"/>
        <stop offset="1" stop-color="var(--tower-blue)"/>
      </radialGradient>
    </defs>
    <circle cx="291" cy="291" r="293" fill="url(#skyGradient)"/>
  </svg>

  <h1 class="title">
    <span class="title__main">GROWTH LEADER</span>
    <span class="title__sub">ASSESSMENT</span>
  </h1>

  <section class="recipient">
    <h2 class="recipient__heading">INSIGHT REPORT FOR</h2>
    <div class="recipient__field"><span class="recipient__label">NAME</span><span class="recipient__line"></span></div>
    <div class="recipient__field"><span class="recipient__label">DATE</span><span class="recipient__line"></span></div>
  </section>

  <div class="brand">
    <div class="brand__name">Northfield<br>Partners</div>
    <div class="brand__tagline">Advisors in Leadership</div>
  </div>
</main>
</body>
</html>
```